Business Card Design

I need a design/ business card for a new company that caters for Event Hire (decorations and linen only) I am dabbling in rustic/ vintage designs for weddings and would like an elegant look to the cards. Something that will catch peoples eyes amongst the rest of the competitions cards and stand out to all fields, corporate/ weddings and general functions.

I am unsure of colours or pictures i would like so i am open to anything but possibly stick away from photos as i they are not more work of art on the card?

Target Market(s)

weddings and corporate events

Industry/Entity Type

Business

Contact Information for Business Card

Marlowe Weddings & Event Hire

Servicing the Gladstone Region for Weddings, Corporate & Private Functions

marloweweddings@postvane.com
Phone: 0427 813 542

Requirements
Must have
• The writing "Marlowe Weddings & Event Hire" please
Nice to have
• Something that really stands out as a must have at your event
Should not have
• Pictures that are not of my work

```html
<!DOCTYPE html>
<html lang="en">
<head>
<meta charset="utf-8">
<title>Marlowe Weddings &amp; Event Hire — Business Card</title>
<link rel="stylesheet" href="https://fonts.googleapis.com/css2?family=Crimson+Text:wght@400;600&display=swap">
<style>
  :root {
    --card-bg: #e4eabb;
    --card-bg-light: #eef1c9;
    --ink: #2b3433;
    --serif: "Crimson Text", Georgia, serif;
  }
  html, body {
    margin: 0;
    padding: 0;
    width: 1200px;
    height: 741px;
    overflow: hidden;
  }
  .card {
    position: relative;
    width: 1200px;
    height: 741px;
    background: radial-gradient(ellipse at 35% 40%, var(--card-bg-light) 0%, var(--card-bg) 70%);
    color: var(--ink);
    font-family: var(--serif);
  }
  .centered {
    position: absolute;
    left: 0;
    width: 1200px;
    text-align: center;
    margin: 0;
    white-space: nowrap;
  }
  .brand-name {
    top: 178px;
    font-size: 118px;
    font-weight: 400;
    letter-spacing: 10px;
    line-height: 1;
  }
  .business-line {
    top: 318px;
    font-size: 49px;
    font-weight: 400;
    line-height: 1;
  }
  .tagline {
    top: 414px;
    font-size: 40px;
    line-height: 1;
    letter-spacing: 0.5px;
  }
  .service-area {
    top: 478px;
    font-size: 23px;
    line-height: 28px;
    letter-spacing: 0.4px;
  }
  .rule {
    position: absolute;
    height: 0;
    border-top: 1.2px solid var(--ink);
  }
  .rule--main { top: 391px; left: 311px; width: 586px; }
  .rule--tagline { top: 472px; left: 375px; width: 458px; }
  .contact {
    position: absolute;
    text-align: center;
  }
  .contact__label {
    font-size: 20px;
    font-weight: 600;
    letter-spacing: 2px;
    line-height: 1;
    padding-bottom: 3px;
    border-bottom: 1.2px solid var(--ink);
  }
  .contact__value {
    margin-top: 3px;
    font-size: 17px;
    line-height: 1;
  }
  .contact--email { top: 585px; left: 311px; width: 248px; }
  .contact--phone { top: 585px; left: 751px; width: 145px; }
  .contact--phone .contact__value { letter-spacing: 3px; font-size: 18px; }
</style>
</head>
<body>
  <main class="card">
    <h1 class="centered brand-name">Marlowe</h1>
    <p class="centered business-line">Weddings &amp; Event Hire</p>
    <div class="rule rule--main"></div>
    <p class="centered tagline">a must have at your event</p>
    <div class="rule rule--tagline"></div>
    <p class="centered service-area">Servicing the Gladstone Region<br>Weddings, Corporate &amp; Private Functions</p>

    <div class="contact contact--email">
      <div class="contact__label">e-mail</div>
      <div class="contact__value">marloweweddings@postvane.com</div>
    </div>
    <div class="contact contact--phone">
      <div class="contact__label">phone</div>
      <div class="contact__value">0427 813 542</div>
    </div>
  </main>
</body>
</html>
```